Bold & Clean Brisk Harbor Stationary Design

Our company, Brisk Harbor Capital Partners needs a business card, letterhead, and envelope design that all also the formatting standards for quickleafpress.com.

Envelope:
Safe Zone: 9.375" x 4"
Trim Size: 9.5" x 4.15"
Bleed Size: 11.125" 8.625"

Letterhead:
Safe Zone: 10.875" x 8.375"
Trim Size: 11" x 8.5"
Bleed Size: 11.125" x 8.625"

Our mailing address is:
2870 W Larkhill St
Chicago, IL 60618

Please make sure the return address on the envelope is formatted correctly for mailing and the logo is not too large.

Please submit designs in word and PDF form.

Our current letterhead is attached.

We would also like a business card with our existing logo that will meet standards for formatting through Quickleaf Press (quickleafpress.com).

These standards are:
Safe Zone: 3.375" x 1.875"
Trim Size: 3.5" x 2"
Bleed Size: 3.625" x 2.125"

The business card is going to be for Marco Lindqvist, President/CEO of Brisk Harbor Capital Partners. Please include the Address, Telephone Number, Cell Phone Number, Fax Number, Email, and Website Address on the card, which are as follows:

2870 W Larkhill St
Chicago, IL 60618

Tel: (773) 555-0172
Cell: (630) 555-0138
Fax: (63) 555-0194
Email: mrl@briskharborcap.com
Web: www.briskharborcap.com

Please make sure that we can easily change the name of the staff member and job position title ourselves as we will be having cards for individual employees in the future as well.

The back of the card should also have the Brisk Harbor logo on it with our services listed:

Financial Planning | Tax | Solutions for Small Businesses

Industry/Entity Type

Accounting

Requirements
Must have
• envelope
• letterhead
• business card
• All meeting standards set out above.

```html
<!DOCTYPE html>
<html lang="en">
<head>
<meta charset="utf-8">
<title>Brisk Harbor Capital Partners — Stationery</title>
<link href="https://fonts.googleapis.com/css2?family=Questrial&family=Crimson+Text:wght@400&display=swap" rel="stylesheet">
<style>
  :root{
    --backdrop:#b5b5b5;
    --paper:#ffffff;
    --orange:#f15a2b;
    --navy:#1f2a55;
    --ink:#222;
    --ghost:#f1f1f1;
  }
  *{margin:0;padding:0;box-sizing:border-box}
  html,body{width:1200px;height:2198px;overflow:hidden;background:var(--backdrop)}
  body{position:relative;font-family:"Questrial",sans-serif;color:var(--ink)}
  .sheet{position:absolute;background:var(--paper);box-shadow:0 2px 8px rgba(0,0,0,.25);overflow:hidden}
  .band{position:absolute;left:0;top:0;bottom:0;background:var(--orange)}
  .band::after{content:"";position:absolute;top:0;bottom:0;right:-5px;width:5px;background:var(--navy)}
  .brand{position:absolute;display:flex;align-items:center;gap:.35em;color:var(--navy);white-space:nowrap}
  .brand .dot{width:.8em;height:.8em;border-radius:50%;background:var(--orange);flex:none}
  .ghost-ring{position:absolute;border-radius:50%;border:14px solid var(--ghost)}

  /* Letterhead */
  .letterhead{left:142px;top:88px;width:916px;height:1187px}
  .letterhead .band{width:34px}
  .letterhead .brand{left:82px;top:48px;font-size:30px}
  .sender{position:absolute;right:42px;top:56px;text-align:right;font-size:12px;line-height:15px}
  .sender strong{font-weight:400;color:#000;letter-spacing:.2px}
  .letter{position:absolute;left:82px;top:204px;width:774px;font-family:"Crimson Text",serif;font-size:15px;line-height:22px;color:#1a1a1a}
  .letter p{margin-bottom:22px}
  .letter .recipient{margin-bottom:22px}
  .signature{width:190px;height:60px;margin:6px 0 10px;background:linear-gradient(90deg,#eee,#f7f7f7)}
  .letterhead .ghost-ring{right:-140px;top:810px;width:520px;height:520px}
  .lh-contact{position:absolute;left:62px;bottom:20px;font-size:11.5px;line-height:15.5px}
  .icon-stack{position:absolute;left:11px;bottom:20px;display:flex;flex-direction:column;gap:3px}
  .icon-stack svg{width:12px;height:12px;fill:#fff}

  /* Envelope */
  .envelope{left:88px;top:1363px;width:1024px;height:442px}
  .envelope .band{width:37px}
  .envelope .brand{left:63px;top:28px;font-size:28px}
  .return-address{position:absolute;left:63px;top:100px;font-size:12px;line-height:15px}
  .envelope .ghost-ring{left:552px;top:62px;width:470px;height:470px}

  /* Business cards */
  .card{top:1895px;width:378px;height:215px}
  .card-back{left:201px}
  .card-back .brand{left:64px;top:78px;font-size:30px}
  .services{position:absolute;left:0;right:0;bottom:22px;text-align:center;font-size:11.5px;color:#111}
  .card-front{left:623px}
  .card-front .band{width:34px}
  .card-front .brand{right:20px;top:22px;font-size:17px}
  .card-front .ghost-ring{right:-20px;top:70px;width:160px;height:160px;border-width:7px}
  .person{position:absolute;left:62px;top:76px}
  .person .name{font-size:13px;letter-spacing:.3px;color:#000}
  .person .title{font-size:10px;letter-spacing:.3px}
  .card-contact{position:absolute;left:62px;top:118px;font-size:10.5px;line-height:14px}
  .card-front .icon-stack{left:11px;bottom:auto;top:118px;gap:4px}
  .card-front .icon-stack svg{width:10px;height:10px}
</style>
</head>
<body>

<section class="sheet letterhead" aria-label="Letterhead">
  <div class="band">
    <div class="icon-stack">
      <svg viewBox="0 0 24 24"><path d="M6.6 10.8a15 15 0 0 0 6.6 6.6l2.2-2.2c.3-.3.7-.4 1-.2 1.1.4 2.3.6 3.6.6.6 0 1 .4 1 1V20c0 .6-.4 1-1 1A17 17 0 0 1 3 4c0-.6.4-1 1-1h3.5c.6 0 1 .4 1 1 0 1.3.2 2.5.6 3.6.1.3 0 .7-.2 1z"/></svg>
      <svg viewBox="0 0 24 24"><path d="M6 3h10v5H6zM4 9h16v8h-3v4H7v-4H4zm5 6v4h6v-4z"/></svg>
      <svg viewBox="0 0 24 24"><path d="M3 5h18v14H3zm2 2v.5l7 5 7-5V7z"/></svg>
      <svg viewBox="0 0 24 24"><path d="M10 14l4-4 1.4 1.4-4 4zM7 12l3-3 1.4 1.4-3 3a2 2 0 0 0 2.8 2.8l3-3 1.4 1.4-3 3A4 4 0 0 1 7 12zm10 0l-3 3-1.4-1.4 3-3a2 2 0 0 0-2.8-2.8l-3 3-1.4-1.4 3-3A4 4 0 0 1 17 12z"/></svg>
    </div>
  </div>
  <div class="brand"><span class="dot"></span>Brisk Harbor</div>
  <address class="sender" style="font-style:normal">
    <strong>Brisk Harbor Capital Partners</strong><br>
    2870 W Larkhill Street<br>
    Chicago, IL 60618
  </address>
  <div class="ghost-ring"></div>
  <div class="letter">
    <p>May 30, 2016</p>
    <div class="recipient">Client Name<br>1149 Fernhollow Rd,<br>Los Angeles, CA 90016</div>
    <p style="margin-bottom:20px">Dear Client:</p>
    <p>Lorem ipsum dolor sit amet, consectetur adipiscing elit. In ullamcorper vel lectus id vestibulum. Mauris rhoncus vitae nulla nec elementum. Suspendisse potenti. Sed lacinia quam erat, ac mattis orci pellentesque vitae. Maecenas justo elit, suscipit varius ullamcorper quis, luctus vitae nisl. Lorem ipsum dolor sit amet, consectetur adipiscing elit. Nullam fringilla orci eu lectus tincidunt rhoncus. Phasellus rutrum facilisis urna id sollicitudin. Sed ac sodales sapien. Fusce viverra aliquet faucibus. Suspendisse commodo diam ac dui ultrices iaculis. Nunc tempus bibendum odio vel sagittis.</p>
    <p>Fusce suscipit sem sit amet elementum dignissim. Ut sit amet massa lectus. Integer consequat sit amet magna ac scelerisque. Curabitur vel mollis est. Cras porttitor volutpat erat, ut fringilla libero. Vestibulum mauris purus, vulputate sit amet rhoncus at, interdum eu odio. Curabitur cursus, enim quis lacinia porta, orci augue malesuada velit, ac rutrum lorem massa vitae velit. Donec a finibus enim. Phasellus ut posuere eros. Nulla molestie sed ex vitae varius. Aenean varius lectus at libero imperdiet malesuada. Nunc id dictum sem diam sit amet lectus dapibus ullamcorper aliquam nisi elifend.</p>
    <p>Mauris vulputate elementum urna eget porttitor. Sed ac lectus posuere, mollis erat sed, facilisis dolor. Curabitur fermentum sed ante vel condimentum. Donec ut mi id nisl volutpat ullamcorper non vel nisl. Nunc rutrum molestie aliquam. Mauris maximus mauris a viverra porta. Fusce ac arcu malesuada, rhoncus sem at, commodo ante. In ac turpis vitae mauris dictum placerat non in metus. Fusce scelerisque, leo eu vulputate eleifend, lorem nulla consectetur lorem, ut rhoncus orci lorem in mauris. Suspendisse ac est nibh nulla venenatis vulputate luctus in ut bibendum ante vitae felis.</p>
    <p style="margin-bottom:0">Best Regards,</p>
    <div class="signature" role="img" aria-label="Handwritten signature of Marco Lindqvist"></div>
    <div>Marco Lindqvist<br>President/CEO</div>
  </div>
  <div class="lh-contact">
    (773) 555-0172<br>(630) 555-0194<br>mrl@briskharborcap.com<br>www.briskharborcap.com
  </div>
</section>

<section class="sheet envelope" aria-label="Envelope">
  <div class="band"></div>
  <div class="brand"><span class="dot"></span>Brisk Harbor</div>
  <address class="return-address" style="font-style:normal">2870 W Larkhill St<br>Chicago, IL 60618</address>
  <div class="ghost-ring"></div>
</section>

<section class="sheet card card-back" aria-label="Business card back">
  <div class="brand"><span class="dot"></span>Brisk Harbor</div>
  <p class="services">Financial Planning &nbsp;|&nbsp; Tax &nbsp;|&nbsp; Solutions for Small Businesses</p>
</section>

<section class="sheet card card-front" aria-label="Business card front">
  <div class="band">
    <div class="icon-stack">
      <svg viewBox="0 0 24 24"><path d="M12 2a7 7 0 0 0-7 7c0 5 7 13 7 13s7-8 7-13a7 7 0 0 0-7-7zm0 9.5A2.5 2.5 0 1 1 12 6.5a2.5 2.5 0 0 1 0 5z"/></svg>
      <svg viewBox="0 0 24 24"><path d="M6.6 10.8a15 15 0 0 0 6.6 6.6l2.2-2.2c.3-.3.7-.4 1-.2 1.1.4 2.3.6 3.6.6.6 0 1 .4 1 1V20c0 .6-.4 1-1 1A17 17 0 0 1 3 4c0-.6.4-1 1-1h3.5c.6 0 1 .4 1 1 0 1.3.2 2.5.6 3.6.1.3 0 .7-.2 1z"/></svg>
      <svg viewBox="0 0 24 24"><path d="M7 2h10v20H7zm2 2v14h6V4z"/></svg>
      <svg viewBox="0 0 24 24"><path d="M6 3h10v5H6zM4 9h16v8h-3v4H7v-4H4zm5 6v4h6v-4z"/></svg>
      <svg viewBox="0 0 24 24"><path d="M3 5h18v14H3zm2 2v.5l7 5 7-5V7z"/></svg>
      <svg viewBox="0 0 24 24"><path d="M10 14l4-4 1.4 1.4-4 4zM7 12l3-3 1.4 1.4-3 3a2 2 0 0 0 2.8 2.8l3-3 1.4 1.4-3 3A4 4 0 0 1 7 12zm10 0l-3 3-1.4-1.4 3-3a2 2 0 0 0-2.8-2.8l-3 3-1.4-1.4 3-3A4 4 0 0 1 17 12z"/></svg>
    </div>
  </div>
  <div class="ghost-ring"></div>
  <div class="brand"><span class="dot"></span>Brisk Harbor</div>
  <div class="person">
    <div class="name">MARCO LINDQVIST</div>
    <div class="title">PRESIDENT/CEO</div>
  </div>
  <div class="card-contact">
    2870 W Larkhill St. Chicago, IL 60618<br>
    (773) 555-0172<br>
    (630) 555-0138<br>
    (630) 555-0194<br>
    mrl@briskharborcap.com<br>
    www.briskharborcap.com
  </div>
</section>

</body>
</html>
```